Quillory Nest Business Card

I need a business card design. We are a collaborate online training company. Our colors are gray and green. Our website is QuilloryNest.com

I would like an area for a profile picture within the card

```html
<!DOCTYPE html>
<html lang="en">
<head>
<meta charset="utf-8">
<title>Quillory Nest Business Card</title>
<link rel="stylesheet" href="https://fonts.googleapis.com/css2?family=Open+Sans:wght@400;600;700&display=swap">
<style>
  :root {
    --backdrop: #e9e7e2;
    --card-white: #ffffff;
    --card-gray: #dcdcdc;
    --ink: #1c1c1c;
    --ink-soft: #3a3a3a;
    --green: #8cc63f;
    --green-light: #c9df78;
    --green-dark: #78ad38;
    --photo-tone: #efb5a6;
    --photo-frame: #3a3a3a;
    --on-green: #ffffff;
  }
  * { margin: 0; padding: 0; box-sizing: border-box; }
  html, body { width: 1200px; height: 1023px; overflow: hidden; }
  body {
    background: var(--backdrop);
    font-family: "Open Sans", Arial, sans-serif;
    position: relative;
  }
  .card {
    position: absolute;
    width: 600px;
    height: 343px;
    border-radius: 16px;
    box-shadow: 0 6px 18px rgba(0,0,0,0.18);
    overflow: hidden;
  }
  .brand {
    position: absolute;
    display: flex; align-items: center; gap: 12px;
  }
  .brand-dot {
    width: 34px; height: 34px; border-radius: 50%;
    background: var(--green);
    flex: none;
  }
  .brand-name {
    font-weight: 700; font-size: 34px; letter-spacing: -0.5px;
    color: var(--ink);
    white-space: nowrap;
  }

  /* Front */
  .card-front {
    left: 60px; top: 90px;
    background: radial-gradient(ellipse at 60% 40%, var(--card-white) 30%, var(--card-gray) 100%);
  }
  .card-front .brand { left: 34px; top: 48px; }
  .profile-photo {
    position: absolute; left: 400px; top: 24px;
    width: 160px; height: 118px;
    background: var(--photo-tone);
    border: 1px solid var(--photo-frame);
  }
  .holder-name {
    position: absolute; right: 40px; top: 150px;
    font-weight: 700; font-size: 22px; line-height: 30px;
    color: var(--green);
  }
  .divider {
    position: absolute; left: 34px; right: 40px; top: 180px;
    height: 1px; background: var(--ink-soft);
  }
  .holder-role {
    position: absolute; right: 40px; top: 185px;
    font-size: 13px; line-height: 18px; color: var(--ink-soft);
  }
  .contacts {
    position: absolute; left: 34px; top: 208px;
    list-style: none;
  }
  .contacts li {
    display: flex; align-items: center; gap: 10px;
    font-size: 14px; color: var(--ink-soft);
    line-height: 27px;
  }
  .contacts svg { width: 14px; height: 14px; flex: none; }
  .address {
    position: absolute; right: 40px; top: 250px;
    text-align: right; font-size: 13px; line-height: 18px;
    color: var(--ink);
  }

  /* Back */
  .card-back {
    left: 540px; top: 580px;
    background: radial-gradient(ellipse at 55% 55%, var(--green-light) 0%, var(--green) 60%, var(--green-dark) 100%);
  }
  .card-back .brand {
    left: 0; right: 0; top: 0; bottom: 0;
    justify-content: center; gap: 18px;
  }
  .card-back .brand-dot {
    width: 58px; height: 58px; background: var(--on-green);
  }
  .card-back .brand-name {
    font-size: 54px; color: var(--on-green);
  }
</style>
</head>
<body>
  <section class="card card-front" aria-label="Business card front">
    <div class="brand">
      <span class="brand-dot"></span>
      <span class="brand-name">Quillory Nest</span>
    </div>
    <div class="profile-photo" role="img" aria-label="Profile picture area for the card holder"></div>
    <div class="holder-name">Your Name</div>
    <div class="divider"></div>
    <div class="holder-role">Owner</div>
    <ul class="contacts">
      <li>
        <svg viewBox="0 0 14 14"><circle cx="7" cy="7" r="6" fill="none" stroke="#8cc63f" stroke-width="1.4"/><path d="M4.5 4.2c.4 2.6 2.6 4.9 5.2 5.3l.6-1.2-1.4-.8-.7.7c-1-.5-1.8-1.3-2.3-2.3l.7-.7-.8-1.4z" fill="#8cc63f"/></svg>
        44-555-01927
      </li>
      <li>
        <svg viewBox="0 0 14 14"><rect x="1" y="3" width="12" height="8" fill="#8cc63f"/><path d="M1 3l6 5 6-5" fill="none" stroke="#fff" stroke-width="1.2"/></svg>
        info@quillorynest.com
      </li>
      <li>
        <svg viewBox="0 0 14 14"><circle cx="7" cy="7" r="6" fill="none" stroke="#8cc63f" stroke-width="1.4"/><path d="M1 7h12M7 1c-3 3-3 9 0 12M7 1c3 3 3 9 0 12" fill="none" stroke="#8cc63f" stroke-width="1"/></svg>
        www.quillorynest.com
      </li>
      <li>
        <svg viewBox="0 0 14 14"><rect x="1" y="1" width="12" height="12" fill="#8cc63f"/></svg>
        social.quillorynest.com/team
      </li>
    </ul>
    <div class="address">Your Address<br>in just two line</div>
  </section>

  <section class="card card-back" aria-label="Business card back">
    <div class="brand">
      <span class="brand-dot"></span>
      <span class="brand-name">Quillory Nest</span>
    </div>
  </section>
</body>
</html>
```